I am looking for label for our Candle Company

We need a label design for our new Candle Company based in Kansas City called Quillet Havren Candle Company. (Pronounced "Kee-Yay"). We want to make sure we get the tick above the "e" in Quillet as Quillet is french for flame. We need a logo that we can use on the candles. We need it to include our name but we need to be able to edit the individual candle scent.

We are looking for a very elegant and vintage/old french look. We do not really want a lot (if any) bright color to the logo/design. I have enclosed our current log (of which we don't really like but are temporarily using) and a design that we love and would like to incorporate. You can see on our current label how we have to be able to include the individual candle scent name. I need to be able to edit this name.

Lise, We have a couple of different label applications that we need to use the design on. We have a small label, a large label and a round label. I will work on getting you the dimensions tomorrow. Do you think there is any way to make a logo out of the middle part of this label? Tobias

Target Market(s)

Anyone who loves candles.

Industry/Entity Type

It Company

Logo Text

Quillet Havren Candle Company

Font styles to use
Decorative
Script

Requirements
Must have
• The ability to edit the candle scent name so that we can use it on every different candle that we make.
Should not have
• Too many vibrant colors.

```html
<!DOCTYPE html>
<html lang="en">
<head>
<meta charset="utf-8">
<title>Quillet Havren Candle Company – Scent Label</title>
<link rel="stylesheet" href="https://fonts.googleapis.com/css2?family=Parisienne&display=swap">
<style>
  :root {
    --rose-brown: #9a4a48;
    --rose-deep: #7f3a3a;
    --rose-soft: #d8aa9c;
    --cream: #f7ead4;
    --cream-light: #fcf2e6;
    --plum-ink: #4a1c2c;
    --rule-violet: #a548a8;
  }
  * { margin: 0; padding: 0; box-sizing: border-box; }
  html, body {
    width: 1200px;
    height: 1194px;
    overflow: hidden;
    background: var(--rose-brown);
  }
  .label {
    position: relative;
    width: 1200px;
    height: 1194px;
    background: linear-gradient(135deg, var(--rose-brown), var(--rose-deep));
    overflow: hidden;
  }
  .label__scroll-frame {
    position: absolute;
    inset: 0;
    background: radial-gradient(ellipse 62% 62% at 50% 50%,
      var(--cream) 0%, var(--cream) 58%, var(--rose-soft) 82%, rgba(154,74,72,0) 100%);
  }
  .label__plate {
    position: absolute;
    left: 247px;
    top: 436px;
    width: 756px;
    height: 292px;
    background: var(--cream-light);
    opacity: 0.9;
  }
  .wordmark {
    position: absolute;
    left: 247px;
    top: 500px;
    width: 756px;
    text-align: center;
    font-family: "Parisienne", cursive;
    font-weight: 400;
    font-size: 52px;
    line-height: 1.2;
    color: var(--plum-ink);
    white-space: nowrap;
  }
  .label__rule {
    position: absolute;
    left: 247px;
    top: 636px;
    width: 756px;
    height: 2px;
    background: var(--rule-violet);
  }
  .scent-name {
    position: absolute;
    left: 247px;
    top: 666px;
    width: 756px;
    text-align: center;
    font-family: "Parisienne", cursive;
    font-weight: 400;
    font-size: 42px;
    line-height: 1.2;
    color: var(--plum-ink);
    white-space: nowrap;
  }
</style>
</head>
<body>
  <main class="label">
    <div class="label__scroll-frame" role="img" aria-label="Ornate cream acanthus scrollwork frame with flourishes around all four edges"></div>
    <div class="label__plate"></div>
    <h1 class="wordmark">Quillet Havren Candle Company</h1>
    <div class="label__rule"></div>
    <p class="scent-name">Girls Night Out</p>
  </main>
</body>
</html>
```